Double Sided Business Card Design for Pet Services

My mom and I want to start a business for pets. We want to offer dog walking, pet sitting as well as boarding and grooming at our home. For the front of the business card, we want a logo that will capture all of our services. We want the name to be Morrito, Inc., which means little paws in Spanish. Perhaps, there could be little paws or just a little paw implemented within the word Morrito. Or we would want a cat and a dog by the word Morrito. We have a cat and a dog at home, and we would be really happy if they could be a part of the business card. It does not have to be anything crazy. Just an outline of a cat or a dog would be awesome. Please see uploaded file.
As for the back of the card, we would want little paws all over the card or we would want a collar, leash, grooming scissor, dog/cat bowl, bone, fish, or toy to show all of the services that we provide. Along with either the many paws or many pet objects, we would want to add our information, such as name (Rosalba Ferrin), telephone numbers (512) 876-2093, e-mail addresses morritoinc@bramwel.com, etc.
We would also want a catch phrase to go on the back of the card, such as "Where all paws matter!" Or "We strive for happy tails." or "A paw-bulous service is guaranteed!"
As for colors, we would not want that many. We would want perhaps white and blue. We would want soft colors that will stand out and make an impression. The same goes with the text. An elegant text would be nice. Or perhaps a text with bold letters. We are excited to see the results, but we are also excited to see your creative ideas and what you will bring to the table.

Target Market(s)

Pet Owners

Contact Information for Business Card

For the front of the business card, we want a logo that will capture all of our services. We want the name to be Morrito, Inc., which means little paws in Spanish. Perhaps, there could be little paws or just a little paw implemented within the word Morrito. Or we would want a cat and a dog by the word Morrito. We have a cat and a dog at home, and we would be really happy if they could be a part of the business card. It does not have to be anything crazy. Just an outline of a cat or a dog would be awesome. Please see uploaded file.
As for the back of the card, we would want little paws all over the card or we would want a collar, leash, grooming scissor, dog/cat bowl, bone, fish, or toy to show all of the services that we provide. Along with either the many paws or many pet objects, we would want to add our information, such as name, telephone numbers, e-mail addresses, etc. We would also want a catch phrase to go on the back of the card, such as "Where all paws matter!" Or "We strive happy tails." or "A paw-bulous service is guaranteed!" Or if there is a way to put the catch phrase in the front of the card. We are open to seeing variety.

Logo Text

Morrito, Inc

Font styles to use
Serif
Script

Colors
ffffff
33a6d7
145ea8

Requirements
Must have
• My project must be a double sided business card.

```html
<!DOCTYPE html>
<html lang="en">
<head>
<meta charset="utf-8">
<title>Morrito, Inc – Business Card</title>
<link href="https://fonts.googleapis.com/css2?family=Arimo:wght@400;700&family=Playball&display=swap" rel="stylesheet">
<style>
  :root{
    --stage:#2a2a2a;
    --green:#5bad6d;
    --green-light:#68ba7c;
    --maroon:#7a2520;
    --white:#ffffff;
    --cat-tone:#c9925a;
    --dog-tone:#d8b98f;
  }
  *{box-sizing:border-box;margin:0;padding:0}
  html,body{width:1200px;height:900px;overflow:hidden;background:var(--stage);font-family:"Arimo",Arial,sans-serif;color:var(--white)}
  .stage{position:relative;width:1200px;height:900px}
  .card{position:absolute;left:320px;width:560px;height:320px;border-radius:22px;overflow:hidden;
    background:radial-gradient(ellipse at 60% 45%,var(--green-light),var(--green) 70%);}
  .card--front{top:70px}
  .card--back{top:510px}
  .edge-stripe{position:absolute;left:0;right:0;bottom:0;height:9px;
    background:linear-gradient(90deg,var(--maroon) 0 38%,var(--white) 38% 100%)}
  .photo{position:absolute;border-radius:45%}
  .photo--cat{background:radial-gradient(circle at 50% 45%,#e0ad73,var(--cat-tone) 60%,rgba(201,146,90,0) 75%)}
  .photo--dog{background:radial-gradient(ellipse at 50% 50%,#f1e2cc,var(--dog-tone) 60%,rgba(216,185,143,0) 75%)}
  .brand-name{position:absolute;font-family:"Playball",cursive;font-weight:400;white-space:nowrap;line-height:1}
  .brand-sub{position:absolute;font-weight:700;white-space:nowrap}
  .website{position:absolute;display:flex;align-items:center;gap:8px;font-size:14px}
  .icon{width:20px;height:20px;flex:none}
  .bubble{position:absolute;left:110px;top:20px;width:128px;height:46px;background:var(--maroon);border-radius:12px;
    display:flex;align-items:center;justify-content:center;text-align:center;font-size:8px;font-weight:700;line-height:1.3;padding:0 10px}
  .bubble-tail{position:absolute;left:176px;top:64px}
  .tagline{position:absolute;font-size:12.5px;font-weight:700;white-space:nowrap}
  .person-name{position:absolute;left:372px;top:86px;font-size:28px;font-weight:700}
  .person-role{position:absolute;left:374px;top:120px;font-size:15px;font-weight:700;color:var(--maroon)}
  .contact-list{position:absolute;left:342px;top:160px;list-style:none;font-size:13.5px;font-weight:700}
  .contact-list li{display:flex;align-items:flex-start;gap:9px;margin-bottom:9px;line-height:1.25}
</style>
</head>
<body>
<div class="stage">

  <section class="card card--front" aria-label="Card front">
    <div class="bubble">A paw-bulous service is guaranteed!</div>
    <svg class="bubble-tail" width="18" height="14" viewBox="0 0 18 14"><path d="M0 0H18L6 14Z" fill="var(--maroon)"/></svg>

    <div class="photo photo--cat" role="img" aria-label="Photo of a tabby cat's head" style="left:78px;top:88px;width:74px;height:70px"></div>
    <div class="brand-name" style="left:158px;top:112px;font-size:48px">Morrito, Inc</div>
    <div class="brand-sub" style="left:232px;top:172px;font-size:22px">Pet service</div>
    <div class="photo photo--dog" role="img" aria-label="Photo of a chihuahua's head" style="left:424px;top:146px;width:112px;height:84px"></div>

    <div class="website" style="left:160px;top:250px">
      <svg class="icon" viewBox="0 0 20 20"><circle cx="10" cy="10" r="10" fill="var(--maroon)"/><g fill="none" stroke="#fff" stroke-width="1.1"><circle cx="10" cy="10" r="5.5"/><ellipse cx="10" cy="10" rx="2.4" ry="5.5"/><path d="M4.5 10h11M5.3 7.3h9.4M5.3 12.7h9.4"/></g></svg>
      <span>MorritoPets.com</span>
    </div>
    <div class="edge-stripe"></div>
  </section>

  <section class="card card--back" aria-label="Card back">
    <div class="photo photo--cat" role="img" aria-label="Photo of a tabby cat's head" style="left:28px;top:40px;width:60px;height:56px"></div>
    <div class="brand-name" style="left:84px;top:62px;font-size:38px">Morrito, Inc</div>
    <div class="brand-sub" style="left:128px;top:110px;font-size:19px">Pet service</div>
    <div class="tagline" style="left:58px;top:140px">A paw-bulous service is guaranteed!</div>
    <div class="photo photo--dog" role="img" aria-label="Photo of a chihuahua's head" style="left:290px;top:56px;width:72px;height:62px"></div>

    <div class="person-name">Your Name</div>
    <div class="person-role">Designation</div>
    <ul class="contact-list">
      <li>
        <svg class="icon" viewBox="0 0 20 20"><circle cx="10" cy="10" r="10" fill="var(--maroon)"/><path d="M7 5.5l1.8 2-1 1.3a7 7 0 0 0 3.4 3.4l1.3-1 2 1.8-1.2 1.6C9.5 14.5 5.5 10.5 5.4 6.7Z" fill="#fff"/></svg>
        <span>(512) 555-0187</span>
      </li>
      <li>
        <svg class="icon" viewBox="0 0 20 20"><circle cx="10" cy="10" r="10" fill="var(--maroon)"/><rect x="5" y="6.5" width="10" height="7" fill="#fff"/><path d="M5 6.5l5 4 5-4" fill="none" stroke="var(--maroon)" stroke-width="1"/></svg>
        <span>hello@morritopets.com</span>
      </li>
      <li>
        <svg class="icon" viewBox="0 0 20 20"><circle cx="10" cy="10" r="10" fill="var(--maroon)"/><path d="M10 4.5a3.6 3.6 0 0 1 3.6 3.6c0 2.7-3.6 7-3.6 7s-3.6-4.3-3.6-7A3.6 3.6 0 0 1 10 4.5Z" fill="#fff"/><circle cx="10" cy="8.2" r="1.3" fill="var(--maroon)"/></svg>
        <span>0000 West Maple Avenue,<br>Dover, DE</span>
      </li>
    </ul>

    <div class="website" style="left:100px;top:258px">
      <svg class="icon" viewBox="0 0 20 20"><circle cx="10" cy="10" r="10" fill="var(--maroon)"/><g fill="none" stroke="#fff" stroke-width="1.1"><circle cx="10" cy="10" r="5.5"/><ellipse cx="10" cy="10" rx="2.4" ry="5.5"/><path d="M4.5 10h11M5.3 7.3h9.4M5.3 12.7h9.4"/></g></svg>
      <span>MorritoPets.com</span>
    </div>
    <div class="edge-stripe"></div>
  </section>

</div>
</body>
</html>
```